Business acrd and Stationery desgin FOR DUNMORE

I want creative and expressive stationary design .on the front side for business card I need the logo and doctors name to be there and on the back side I need time and appointment .Please see attached business card to use same names ,but use address below and phone number

Note:the deigner must submit the file in vector format and PSD and PDF

Business name is :Dunmore Glen Medical Clinic.

Address:
20418 57 ST NW
City :EDMONTON AB
Postal code: T6K 3R8

Phone :(780) 555-0142
Fax:(780) 555-0187

Other Business name :Dunmore Medical Clinic

• logo in the back on business card

```html
<!DOCTYPE html>
<html lang="en">
<head>
<meta charset="utf-8">
<title>Dunmore Glen Medical Clinic – Stationery</title>
<link rel="stylesheet" href="https://fonts.googleapis.com/css2?family=Cinzel:wght@600&family=Arimo:wght@400;700&family=Michroma&display=swap">
<style>
  :root{
    --blue:#2f4f9f;
    --red:#e8353b;
    --paper:#ffffff;
    --ground:#ececec;
    --ink:#3a3a3a;
    --muted:#777;
  }
  *{margin:0;padding:0;box-sizing:border-box}
  html,body{width:1200px;height:937px;overflow:hidden;background:var(--ground)}
  .sheet{position:absolute;background:var(--paper);overflow:hidden}
  .band{position:absolute;left:0;width:100%;display:block}
  .brand{display:flex;flex-direction:column;align-items:center;text-align:center}
  .brand__dot{width:10px;height:10px;border-radius:50%;background:var(--red);margin-bottom:4px}
  .brand__name{font-family:'Cinzel',serif;font-weight:600;color:var(--blue);line-height:1.05;letter-spacing:.02em}
  .web{font-family:'Michroma',sans-serif;letter-spacing:.12em}

  /* letterhead */
  .letterhead{left:184px;top:66px;width:389px;height:546px}
  .letterhead .brand{position:absolute;left:30px;top:32px;width:100px}
  .letterhead .brand__name{font-size:10px}
  .letter{position:absolute;left:37px;top:140px;width:300px;font-family:'Arimo',sans-serif;font-size:4.7px;line-height:1.55;color:var(--ink)}
  .letter p{margin-bottom:9px}
  .letter .gap{margin-bottom:22px}
  .signature{width:22px;height:14px;background:#d8d8d8;margin:4px 0 6px}
  .letter strong{font-weight:700}
  .contact-row{position:absolute;top:506px;left:0;width:100%;font-family:'Michroma',sans-serif;font-size:5.6px;color:var(--ink);line-height:1.7}
  .contact-row span{position:absolute;top:0}

  /* cover sheet */
  .cover{left:635px;top:40px;width:459px;height:576px}
  .cover .brand{position:absolute;left:0;width:100%;top:225px}
  .cover .brand__dot{width:22px;height:22px;margin-bottom:10px}
  .cover .brand__name{font-size:30px}
  .cover .web{position:absolute;top:554px;left:0;width:100%;text-align:center;font-size:9px;color:#333}

  /* business cards */
  .card{left:45px;width:177px;height:100px}
  .card--front{top:658px}
  .card--back{top:783px}
  .card--front .brand{position:absolute;left:8px;top:8px;width:62px}
  .card--front .brand__dot{width:5px;height:5px;margin-bottom:2px}
  .card--front .brand__name{font-size:6.5px}
  .person{position:absolute;right:8px;top:18px;text-align:right;font-family:'Arimo',sans-serif}
  .person__name{font-size:7px;font-weight:700;color:#222;letter-spacing:.04em}
  .person__role{font-size:3.6px;color:var(--muted);letter-spacing:.05em}
  .card-contacts{position:absolute;top:72px;left:0;width:100%;font-family:'Arimo',sans-serif;font-size:3.8px;line-height:1.6;color:var(--ink)}
  .card-contacts span{position:absolute;top:0}
  .card--back .brand{position:absolute;left:0;width:100%;top:26px}
  .card--back .brand__dot{width:7px;height:7px;margin-bottom:3px}
  .card--back .brand__name{font-size:10px}

  /* envelopes */
  .envelope{left:265px;top:672px;width:432px;height:208px}
  .envelope .brand{position:absolute;left:18px;top:30px;width:120px}
  .envelope .brand__dot{width:8px;height:8px}
  .envelope .brand__name{font-size:12px}
  .envelope .web{position:absolute;top:194px;left:0;width:100%;text-align:center;font-size:7px;color:#333}
  .envelope-back{left:737px;top:671px;width:431px;height:209px}
  .flap{position:absolute;left:0;top:0;width:100%;height:72px;background:var(--blue);border-radius:0 0 44px 44px}
  .flap .web{position:absolute;top:30px;left:0;width:100%;text-align:center;font-size:8.5px;color:#1f2f5c;letter-spacing:.3em}
</style>
</head>
<body>

<!-- Letterhead -->
<section class="sheet letterhead" aria-label="Letterhead">
  <div class="brand"><span class="brand__dot"></span><span class="brand__name">Dunmore Glen<br>Medical Clinic</span></div>
  <div class="letter">
    <p>July 2, 2012<br><br><strong>Dear Client,</strong><br>20418 57 ST NW, Edmonton AB</p>
    <p class="gap">Thank you for choosing our clinic for your family's care. This letter confirms the details of your upcoming visit and explains what to bring on the day. Please arrive ten minutes early with your health card and a list of current medications so our team can update your chart before you see the doctor. We look forward to meeting you.</p>
    <p class="gap">If you need to change your appointment, please call our front desk at least one day ahead so we can offer the time to another patient.</p>
    <p>Our clinic offers walk-in care, family medicine and routine checkups six days a week. Evening hours are available on weekdays for patients who work during the day. Lab requisitions, prescription renewals and referrals can be handled during your visit. Should you have any questions before then, our staff will be glad to help you by phone or email.</p>
    <p>Best Regards,</p>
    <div class="signature" role="img" aria-label="Handwritten signature"></div>
    <p><strong>Arlen Price</strong><br>Director<br><br>20418 57 ST NW, Edmonton AB</p>
  </div>
  <svg class="band" style="top:487px" width="389" height="16" viewBox="0 0 389 16">
    <rect width="389" height="16" fill="var(--blue)"/>
    <polygon points="116,0 124,0 132,8 124,16 116,16 124,8" fill="#fff"/>
    <polygon points="277,0 285,0 293,8 285,16 277,16 285,8" fill="#fff"/>
    <g fill="none" stroke="#fff" stroke-width="1">
      <circle cx="49" cy="8" r="4.5"/><ellipse cx="49" cy="8" rx="2" ry="4.5"/><line x1="44.5" y1="8" x2="53.5" y2="8"/>
    </g>
    <path d="M202 3.5a3 3 0 0 1 3 3c0 2.2-3 6-3 6s-3-3.8-3-6a3 3 0 0 1 3-3z" fill="#fff"/>
    <rect x="335.5" y="3" width="5" height="9" rx="1" fill="none" stroke="#fff" stroke-width="1"/>
  </svg>
  <div class="contact-row">
    <span style="left:12px">care@dunmoreglen.ca<br>www.dunmoreglen.ca</span>
    <span style="left:172px">20418 57 ST NW<br>Edmonton AB T6K 3R8</span>
    <span style="left:314px">(780) 555-0142<br>(780) 555-0187</span>
  </div>
  <svg class="band" style="top:535px" width="389" height="11"><rect width="389" height="11" fill="var(--red)"/></svg>
</section>

<!-- Cover sheet -->
<section class="sheet cover" aria-label="Cover sheet">
  <svg class="band" style="top:0" width="459" height="26" viewBox="0 0 459 26">
    <rect width="459" height="26" fill="var(--blue)"/>
    <polygon points="118,0 126,0 139,13 126,26 118,26 131,13" fill="#fff"/>
    <polygon points="348,0 356,0 369,13 356,26 348,26 361,13" fill="#fff"/>
  </svg>
  <div class="brand"><span class="brand__dot"></span><span class="brand__name">Dunmore Glen<br>Medical Clinic</span></div>
  <svg class="band" style="top:550px" width="459" height="26" viewBox="0 0 459 26">
    <rect width="459" height="26" fill="var(--red)"/>
    <polygon points="120,0 338,0 350,13 338,26 120,26 108,13" fill="#fff"/>
  </svg>
  <div class="web">www.dunmoreglen.ca</div>
</section>

<!-- Business card front -->
<section class="sheet card card--front" aria-label="Business card front">
  <div class="brand"><span class="brand__dot"></span><span class="brand__name">Dunmore Glen<br>Medical Clinic</span></div>
  <div class="person"><div class="person__name">DANA WHITLOW</div><div class="person__role">GENERAL PRACTITIONER</div></div>
  <svg class="band" style="top:47px" width="177" height="17" viewBox="0 0 177 17">
    <rect width="177" height="17" fill="var(--blue)"/>
    <polygon points="51,0 55,0 61,8.5 55,17 51,17 57,8.5" fill="#fff"/>
    <polygon points="111,0 115,0 121,8.5 115,17 111,17 117,8.5" fill="#fff"/>
    <g fill="none" stroke="#fff" stroke-width=".8">
      <circle cx="22" cy="8.5" r="4"/><ellipse cx="22" cy="8.5" rx="1.8" ry="4"/><line x1="18" y1="8.5" x2="26" y2="8.5"/>
    </g>
    <path d="M88 4a2.6 2.6 0 0 1 2.6 2.6c0 2-2.6 5.4-2.6 5.4s-2.6-3.4-2.6-5.4A2.6 2.6 0 0 1 88 4z" fill="#fff"/>
    <rect x="147" y="4" width="4.5" height="8.5" rx=".8" fill="none" stroke="#fff" stroke-width=".8"/>
  </svg>
  <div class="card-contacts">
    <span style="left:4px">care@dunmoreglen.ca<br>www.dunmoreglen.ca</span>
    <span style="left:73px">20418 57 ST NW<br>Edmonton AB T6K 3R8</span>
    <span style="left:137px">(780) 555-0142<br>(780) 555-0187</span>
  </div>
  <svg class="band" style="top:95px" width="177" height="5"><rect width="177" height="5" fill="var(--red)"/></svg>
</section>

<!-- Business card back -->
<section class="sheet card card--back" aria-label="Business card back">
  <svg class="band" style="top:0" width="177" height="9" viewBox="0 0 177 9">
    <rect width="177" height="9" fill="var(--blue)"/>
    <polygon points="38,0 42,0 46,4.5 42,9 38,9 42,4.5" fill="#fff"/>
    <polygon points="132,0 136,0 140,4.5 136,9 132,9 136,4.5" fill="#fff"/>
  </svg>
  <div class="brand"><span class="brand__dot"></span><span class="brand__name">Dunmore Glen<br>Medical Clinic</span></div>
  <svg class="band" style="top:92px" width="177" height="10" viewBox="0 0 177 10">
    <rect width="177" height="10" fill="var(--red)"/>
    <polygon points="38,0 42,0 46,5 42,10 38,10 42,5" fill="#fff"/>
    <polygon points="132,0 136,0 140,5 136,10 132,10 136,5" fill="#fff"/>
  </svg>
</section>

<!-- Envelope front -->
<section class="sheet envelope" aria-label="Envelope front">
  <svg class="band" style="top:0" width="432" height="19" viewBox="0 0 432 19">
    <rect width="432" height="19" fill="var(--blue)"/>
    <polygon points="116,0 123,0 132,9.5 123,19 116,19 125,9.5" fill="#fff"/>
    <polygon points="320,0 327,0 336,9.5 327,19 320,19 329,9.5" fill="#fff"/>
  </svg>
  <div class="brand"><span class="brand__dot"></span><span class="brand__name">Dunmore Glen<br>Medical Clinic</span></div>
  <svg class="band" style="top:190px" width="432" height="18" viewBox="0 0 432 18">
    <rect width="432" height="18" fill="var(--red)"/>
    <polygon points="97,0 319,0 310,9 319,18 97,18 88,9" fill="#fff"/>
  </svg>
  <div class="web">www.dunmoreglen.ca</div>
</section>

<!-- Envelope back -->
<section class="sheet envelope-back" aria-label="Envelope back">
  <div class="flap"><div class="web">www.dunmoreglen.ca</div></div>
</section>

</body>
</html>
```